Veltrane Partners Website - developing a website for a new IIoT (Industrial Internet of Things) startup

Hi All-

Thought I'd re-write this bit...

Firstly, to everyone who has submitted designs, thank you.

Basically, we are looking for a simple/ elegant / modern website with clean lines and design. Because this is a startup, we don't have a great deal of content. Therefore, I'm relying on the site to give us an established / international feel (no images of London, London attractions, or the London skyline please!) We will have offices in London / LA and Tokyo by the end of this year.

Selecting great images is really important. As I say, abstract is fine (less literal.) Black and white is fine as well. We need to convey our expertise to new, international clients, so this is v.important.

http://www.pellucora41.it/ (favourite)
http://www.craftonvelmo.com/cases/

In terms of colour, I think white /grey/ black and maybe experiment with red for the word Veltrane and (possibly) Group. Please note** I need the following words / strap line written underneath the main logo: IIoT Strategy. Sensor Innovation. Machine Learning.

Whomever we chose to work with, this will be an ongoing partnership: we will continually need to add new content and update the site.

Thank you!

Tam.
Updates

**Please view updated brief description.

Target Market(s)

Mid-sized (£25M- £500M GBP) companies in the UK/ US and Asia. Facilities/ Construction/ Automotive/ Manufacturing / Engineering

Industry/Entity Type

Information Technology

Logo Text

Veltrane Partners -- IIoT Strategy. Sensor Innovation. Machine Learning (written underneath)

Coding

Coded - Design and coding required

Number of Pages Required

5+ page

Font styles to use
Sans Serif

Requirements
Must have
• An international, established, aspirational feel. Beautiful imagery. elegant infographics (nothing complex). CTA on homepage.
Should not have
• Anything cartoony / informal or naff corporate imagery.

```html
<!DOCTYPE html>
<html lang="en">
<head>
<meta charset="utf-8">
<title>Veltrane Partners</title>
<link href="https://fonts.googleapis.com/css2?family=Open+Sans:wght@400;600;700&family=Raleway:wght@300;400;600&display=swap" rel="stylesheet">
<style>
:root{
  --red:#e2282b;
  --ink:#222;
  --text:#6d6d6d;
  --panel:#f3f3f3;
  --footer:#f1f1f1;
  --line:#dcdcdc;
}
*{box-sizing:border-box;margin:0;padding:0}
html,body{width:1200px;height:3748px;overflow:hidden;background:#fff}
body{position:relative;font-family:"Open Sans",sans-serif;color:var(--text)}
.abs{position:absolute}
.brand{left:160px;top:30px;display:flex;align-items:center;gap:14px}
.brand-mark{width:44px;height:44px;border-radius:50%;background:var(--red)}
.brand-name{font-family:"Raleway",sans-serif;font-weight:600;font-size:30px;color:var(--red);letter-spacing:1px;line-height:1}
.brand-tag{font-size:12px;color:#555;margin-top:5px}
.menu{left:1010px;top:56px;width:26px}
.menu span{display:block;height:3px;background:var(--ink);margin-bottom:5px}
.hero{left:160px;top:140px;width:880px;height:452px;background:linear-gradient(180deg,#7fa8d6 0%,#b9d1ec 40%,#eef3f8 65%,#9fb8d4 100%)}
.hero-text{left:160px;top:380px;width:880px;text-align:center;color:#fff;font-family:"Raleway",sans-serif;font-weight:600;font-size:28px;line-height:38px;text-transform:uppercase;text-shadow:0 1px 4px rgba(0,0,0,.35)}
.intro{left:260px;top:660px;width:680px;text-align:center;font-size:15px;line-height:24px}
.intro p{margin-bottom:18px}
.panel{background:var(--panel)}
.title{font-family:"Raleway",sans-serif;font-weight:400;font-size:50px;color:var(--red);letter-spacing:2px;text-transform:uppercase;line-height:1}
.copy{font-size:15px;line-height:23px}
.copy p{margin-bottom:18px}
.more{font-size:15px;font-weight:700;color:var(--ink);border-bottom:2px solid var(--red);padding-bottom:3px}
.post{display:flex;gap:14px;width:390px}
.date{width:44px;height:48px;background:var(--red);color:#fff;text-align:center;font-size:12px;font-weight:700;line-height:16px;padding-top:8px;flex:none}
.post h4{font-size:13px;color:var(--ink);font-weight:700;line-height:18px}
.post p{font-size:12px;line-height:17px}
.dot{width:14px;height:14px;border-radius:50%;border:2px solid #999}
.field{left:665px;width:375px;border-bottom:1px solid var(--line);font-size:12px;color:#aaa;padding-bottom:8px}
.footer{left:0;top:3510px;width:1200px;height:238px;background:var(--footer)}
.nav{left:160px;top:3540px;display:flex;gap:36px;font-size:14px;color:#555}
.nav .on{color:var(--ink);font-weight:700;border-bottom:2px solid var(--red);padding-bottom:4px}
.follow{left:800px;top:3536px;display:flex;align-items:center;gap:8px;font-size:14px;color:#555}
.soc{width:22px;height:22px;border-radius:50%;background:var(--red)}
.contact{display:flex;gap:12px;font-size:13px;line-height:19px;color:#555}
.contact b{color:var(--ink);display:block}
.ico{width:28px;height:28px;border-radius:50%;background:var(--red);flex:none;display:flex;align-items:center;justify-content:center}
.rule{left:160px;top:3690px;width:880px;border-top:1px solid var(--line)}
.copyright{left:0;top:3712px;width:1200px;text-align:center;font-size:12px;color:#888}
</style>
</head>
<body>
<header>
  <div class="abs brand">
    <div class="brand-mark"></div>
    <div>
      <div class="brand-name">VELTRANE PARTNERS</div>
      <div class="brand-tag">IIoT Strategy • Sensor Innovation<br>• Machine Learning</div>
    </div>
  </div>
  <div class="abs menu"><span></span><span></span><span></span></div>
</header>

<div class="abs hero" role="img" aria-label="Ladder rising into bright clouds against a blue sky"></div>
<h1 class="abs hero-text">We focus on helping our clients to<br>explore new business models &amp; also<br>improve their relationships with their<br>clients using data</h1>

<section class="abs intro">
  <p>The core team at Veltrane Partners are Innovators, Engineers, PhDs and Data Scientists who assist mid-sized companies (£25M-£500M) to capitalise on the enormous potential of the Industrial Internet of Things ("IIoT").</p>
  <p>Our three business units, Strategy, Sensors and AI – mean that we can provide expert advice to both new entrants and companies already familiar with IIoT.</p>
</section>

<div class="abs panel" style="left:560px;top:850px;width:640px;height:480px"></div>
<div class="abs" style="left:40px;top:900px;width:480px;height:400px;background:linear-gradient(135deg,#0d3b66,#1d5f9a 60%,#0b2c4d)" role="img" aria-label="Chess king beside a target with an arrow in the bullseye"></div>
<h2 class="abs title" style="left:625px;top:940px">Strategy</h2>
<div class="abs copy" style="left:625px;top:1010px;width:430px">
  <p>The Strategy team work with customers to navigate the complex world of IoT and develop world class strategies for maximising value. We know that connecting assets is not appropriate for every business, sometimes the challenges outweigh the rewards.</p>
  <p>However, where an IIoT strategy is appropriate we have the right team to help your company clarify its visions.</p>
</div>
<a class="abs more" style="left:625px;top:1232px">Read More</a>

<div class="abs panel" style="left:0;top:1390px;width:620px;height:490px"></div>
<div class="abs" style="left:615px;top:1420px;width:535px;height:370px;background:linear-gradient(135deg,#10284a,#1e4f86 55%,#2b6fa8)" role="img" aria-label="Connected smart city of buildings, vehicles and sensors"></div>
<h2 class="abs title" style="left:160px;top:1540px">Sensors</h2>
<div class="abs copy" style="left:160px;top:1610px;width:410px">
  <p>The Sensor team are focused on innovation using Sensors and MEMS (Micro Electromechanical Systems). We view ourselves as the conduit between the vast array of complex sensors and their potential applications in the "real world."</p>
  <p>Our focus is looking at sensor deployments for Buildings, Environment, Factories, Parking, Agriculture, Water, Air and Health.</p>
</div>
<a class="abs more" style="left:160px;top:1850px">Read More</a>

<div class="abs panel" style="left:560px;top:2010px;width:640px;height:550px"></div>
<div class="abs" style="left:40px;top:2100px;width:480px;height:400px;background:linear-gradient(180deg,#eef0f2,#cfd6dd 55%,#3c4f66)" role="img" aria-label="Data dashboards with charts on screens below a mountain range"></div>
<h2 class="abs title" style="left:625px;top:2140px">Data &amp; AI</h2>
<div class="abs copy" style="left:625px;top:2210px;width:430px">
  <p>The Data &amp; AI team focus on getting the maximum value from our customer's sensors. We are a small team of engineers and data scientists who know that the real value from IoT comes from the quality of sensor data. We monitor and analyse this data and then deliver it to our customers via stunning dashboards.</p>
</div>
<a class="abs more" style="left:625px;top:2390px">Read More</a>

<div class="abs" style="left:160px;top:2832px;width:376px;height:208px;background:linear-gradient(135deg,#e7a24a,#c9603c 55%,#3a4a5c)" role="img" aria-label="Team working together around a desk seen from above"></div>
<h2 class="abs title" style="left:160px;top:3080px">Blogs</h2>
<div class="abs dot" style="left:488px;top:3090px;border-color:#ccc"></div>
<div class="abs dot" style="left:510px;top:3090px"></div>
<div class="abs post" style="left:160px;top:3160px">
  <div class="date">26<br>Feb</div>
  <div><h4>Retrofitting sensors in mid-sized plants</h4><p>Practical steps for connecting legacy assets without halting production lines. <span style="color:var(--red)">[+]</span></p></div>
</div>
<div class="abs post" style="left:160px;top:3250px">
  <div class="date">26<br>Feb</div>
  <div><h4>Turning machine data into daily decisions</h4><p>How clear dashboards help site teams act faster on live sensor readings. <span style="color:var(--red)">[+]</span></p></div>
</div>
<a class="abs more" style="left:460px;top:3372px">Read More</a>

<div class="abs panel" style="left:600px;top:2650px;width:600px;height:800px"></div>
<div class="abs" style="left:665px;top:2760px;width:375px;height:280px;background:radial-gradient(circle at 50% 45%,#d2262b,#7a1215 45%,#111 80%)" role="img" aria-label="Red event invitation box glowing on a dark background"></div>
<h2 class="abs title" style="left:665px;top:3080px">Events</h2>
<p class="abs copy" style="left:665px;top:3145px;width:360px;font-size:13px;line-height:20px">We will be launching some exclusive invite-only events in 2018. If you would like to know, please enter your email address here.</p>
<div class="abs field" style="top:3225px">Email Address</div>
<a class="abs more" style="left:665px;top:3268px;font-size:13px">Submit</a>

<footer>
  <div class="abs footer"></div>
  <nav class="abs nav"><span class="on">About</span><span>Strategy</span><span>Sensors</span><span>Data &amp; AI</span><span>Events</span><span>Blogs</span><span>Contact</span></nav>
  <div class="abs follow">Follow Us On :<span class="soc"></span><span class="soc"></span><span class="soc"></span><span class="soc"></span><span class="soc"></span></div>
  <div class="abs contact" style="left:160px;top:3610px">
    <div class="ico"><svg width="12" height="16" viewBox="0 0 12 16"><path d="M6 0a6 6 0 0 0-6 6c0 4.5 6 10 6 10s6-5.5 6-10a6 6 0 0 0-6-6zm0 8.5A2.5 2.5 0 1 1 6 3.5a2.5 2.5 0 0 1 0 5z" fill="#fff"/></svg></div>
    <div>1820 Harborline Road NE, Building B,<br>Suite 410, Marlow City, GA 30999</div>
  </div>
  <div class="abs contact" style="left:540px;top:3610px">
    <div class="ico"><svg width="14" height="14" viewBox="0 0 14 14"><path d="M3 0l2.5 3.5-1.5 1.8a8 8 0 0 0 4.7 4.7L10.5 8.5 14 11l-1.5 2.5C6 14 0 8 .5 1.5z" fill="#fff"/></svg></div>
    <div><b>Phone</b>+1 555-014-2290</div>
  </div>
  <div class="abs contact" style="left:800px;top:3610px">
    <div class="ico"><svg width="14" height="10" viewBox="0 0 14 10"><rect width="14" height="10" fill="#fff"/><path d="M0 0l7 5 7-5" stroke="#e2282b" fill="none"/></svg></div>
    <div><b>Email us :</b>hello@veltranepartners.com</div>
  </div>
  <div class="abs rule"></div>
  <div class="abs copyright">Copyright © Veltrane Partners. All Rights Reserved</div>
</footer>
</body>
</html>
```